Frostwyn.co - Polar Expeditions Specialists

We need a modern, visually striking business card for Frostwyn.co, a company specialized in selling expedition cruises to the most remote regions on Earth, with a focus on the Arctic and Antarctica. The design should instantly communicate that the cardholder is an expert in polar travel. Use clean, premium aesthetics with cool tones like icy blue and white, possibly incorporating polar imagery (ice, glaciers, penguins, etc.)

Attached the logo

Contact Information for Business Card

Feels high-end and trustworthy.. Visually memorable — encourages people to keep it

Colors
0054AA
0677BA
7BADD7
CADEEF
E8F1F8

Requirements
Must have
• ice, glaciers, penguins, montains
Nice to have
• modern, transparente,

```html
<!DOCTYPE html>
<html lang="en">
<head>
<meta charset="UTF-8">
<title>Frostwyn.co — Business Card</title>
<link href="https://fonts.googleapis.com/css2?family=Poppins:wght@600;800&family=Roboto:wght@300;400&display=swap" rel="stylesheet">
<style>
  :root{
    --page:#16181c;
    --card-deep:#070f24;
    --card-mid:#0b1a45;
    --card-glow:#122a78;
    --brand:#3a86d8;
    --brand-soft:#7badd7;
    --edge:#2a62c9;
    --ink:#e8f1f8;
    --rule:#cadeef;
  }
  *{margin:0;padding:0;box-sizing:border-box}
  html,body{width:1200px;height:840px;overflow:hidden;background:var(--page)}
  .canvas{position:relative;width:1200px;height:840px}
  .card{
    position:absolute;width:600px;height:343px;border-radius:22px;overflow:hidden;
    background:radial-gradient(circle at 62% 55%,var(--card-glow) 0%,var(--card-mid) 35%,var(--card-deep) 80%);
    box-shadow:0 0 0 2px var(--edge),0 24px 50px rgba(0,0,0,.55);
  }
  .card--front{left:150px;top:50px}
  .card--back{left:450px;top:447px}

  .polar-scene{
    position:absolute;left:60px;top:95px;width:390px;height:248px;
    border-radius:46% 46% 0 0;
    background:radial-gradient(ellipse at 72% 70%,#2a3d9a 0%,#15245e 35%,#08122e 75%);
    opacity:.9;
  }
  .brand{font-family:"Poppins",sans-serif;color:var(--brand)}
  .brand__name{font-weight:800;letter-spacing:-.5px;line-height:1}
  .brand__tag{font-weight:600;line-height:1.1}

  .card--front .brand{position:absolute;right:40px;top:48px;text-align:right}
  .card--front .brand__name{font-size:56px}
  .card--front .brand__tag{font-size:15px;margin-top:4px}

  .card--back .brand{position:absolute;right:34px;top:60px;text-align:right}
  .card--back .brand__mark{display:inline-block;width:44px;height:44px;border-radius:50%;background:var(--brand);margin-bottom:10px}
  .card--back .brand__name{font-size:50px}
  .card--back .brand__tag{font-size:13px;margin-top:4px}

  .divider{position:absolute;left:50px;right:34px;top:232px;height:1px;background:var(--rule)}

  .person{position:absolute;left:50px;top:182px;font-family:"Roboto",sans-serif}
  .person__name{color:var(--brand);font-size:20px;font-weight:400;letter-spacing:.3px}
  .person__role{color:var(--ink);font-size:17px;font-weight:300;margin-top:2px}

  .contacts{position:absolute;left:60px;top:246px;list-style:none;font-family:"Roboto",sans-serif;color:var(--ink);font-size:15px;font-weight:300}
  .contacts li{display:flex;align-items:center;gap:10px;height:24px}
  .contacts svg{width:13px;height:13px;flex:none}

  .address{position:absolute;right:34px;top:252px;text-align:right;font-family:"Roboto",sans-serif;color:var(--ink);font-size:15px;font-weight:300;line-height:1.35}
</style>
</head>
<body>
<main class="canvas">
  <section class="card card--front">
    <div class="polar-scene" role="img" aria-label="Polar bear and penguin silhouettes under a starry night sky"></div>
    <div class="brand">
      <div class="brand__name">Frostwyn.co</div>
      <div class="brand__tag">Polar Expeditions Specialists</div>
    </div>
  </section>

  <section class="card card--back">
    <div class="brand">
      <span class="brand__mark"></span>
      <div class="brand__name">Frostwyn.co</div>
      <div class="brand__tag">Polar Expeditions Specialists</div>
    </div>
    <div class="person">
      <div class="person__name">ELIAS VARDEN</div>
      <div class="person__role">Manager</div>
    </div>
    <div class="divider"></div>
    <ul class="contacts">
      <li><svg viewBox="0 0 24 24" fill="#3a86d8"><path d="M6.6 10.8a15 15 0 0 0 6.6 6.6l2.2-2.2c.3-.3.7-.4 1-.2 1.1.4 2.3.6 3.6.6.6 0 1 .4 1 1V20c0 .6-.4 1-1 1A17 17 0 0 1 3 4c0-.6.4-1 1-1h3.5c.6 0 1 .4 1 1 0 1.3.2 2.5.6 3.6.1.3 0 .7-.2 1z"/></svg>123-456-2100</li>
      <li><svg viewBox="0 0 24 24" fill="none" stroke="#3a86d8" stroke-width="2"><rect x="2" y="5" width="20" height="14" rx="1"/><path d="M2 6l10 7 10-7"/></svg>hello@frostwyn.co</li>
      <li><svg viewBox="0 0 24 24" fill="none" stroke="#3a86d8" stroke-width="2"><circle cx="12" cy="12" r="10"/><path d="M2 12h20M12 2c3 3 3 17 0 20M12 2c-3 3-3 17 0 20"/></svg>www.frostwyn.co</li>
    </ul>
    <div class="address">Your address<br>city, state, ZIP 0000</div>
  </section>
</main>
</body>
</html>
```